Summit Relay Business Card

Side 1: Summit Relay Logo (logo without Maltese cross) with industrial rope rescue related theme. Our company services - TRAINING - Fire Training, Confined Space Rescue Training, Rope Rescue training, Hazmat Training, Incident Command, EMS, Pump Operations Training. Website - summitrelay-example.com.
Side 2: Summit Relay Fire Department Logo (logo with Maltese cross) with Firefighter related theme. Company (division) services - FIELD SERVICES - Fire Department, Stand-by Rescue, Safety, EMS, Planning. "Supporting the Emergency Response Community Since 1967"

Add contact information wherever it makes since (Name, Email, Phone).
I would like it to represent the Summit Relay Fire Department Logo as a division not as a separate entity without saying it, possibly by depicting it in the background of Side 2 instead of being a standalone picture like the logo on Side 1.

```html
<!DOCTYPE html>
<html lang="en">
<head>
<meta charset="utf-8">
<title>Summit Relay Business Card</title>
<link rel="stylesheet" href="https://fonts.googleapis.com/css2?family=Lato:wght@400;700;900&family=Montserrat:wght@700;800;900&display=swap">
<style>
  :root {
    --red: #f01418;
    --red-soft: #f6c9c7;
    --black: #1c1c1c;
    --white: #ffffff;
    --paper: #f4f4f4;
    --stage: #2b2b2b;
  }
  * { box-sizing: border-box; margin: 0; padding: 0; }
  html, body { width: 1200px; height: 924px; overflow: hidden; background: var(--stage); }
  .canvas { position: relative; width: 1200px; height: 924px; }

  .card {
    position: absolute;
    width: 700px; height: 400px;
    overflow: hidden;
    box-shadow: 0 14px 30px rgba(0,0,0,.45);
  }

  /* ---------- Side 1 : training ---------- */
  .card--training { left: 60px; top: 50px; background: var(--black); color: var(--white); font-family: "Lato", sans-serif; }
  .brand-lockup { position: absolute; left: 60px; top: 130px; display: flex; align-items: center; gap: 14px; }
  .brand-lockup__mark { width: 20px; height: 20px; background: var(--red); flex: none; }
  .brand-lockup__name {
    font-family: "Montserrat", sans-serif; font-weight: 900;
    font-size: 36px; letter-spacing: 1px; color: var(--red); line-height: 1.05;
    white-space: nowrap;
  }
  .brand-rule { position: absolute; left: 60px; top: 226px; width: 240px; height: 3px; background: var(--red); }

  .training { position: absolute; left: 370px; top: 66px; }
  .training__title {
    font-family: "Montserrat", sans-serif; font-weight: 900; font-size: 22px;
    color: var(--red); letter-spacing: .5px; margin-bottom: 12px; white-space: nowrap;
  }
  .tick-list { list-style: none; }
  .tick-list li { display: flex; align-items: center; gap: 9px; font-size: 15px; line-height: 27px; white-space: nowrap; }
  .tick-list svg { width: 14px; height: 14px; flex: none; }

  .website {
    position: absolute; left: 330px; top: 340px;
    font-family: "Montserrat", sans-serif; font-weight: 700; font-size: 12px;
    letter-spacing: 3px; color: var(--red); white-space: nowrap;
  }

  /* ---------- Side 2 : field services ---------- */
  .card--field { left: 440px; top: 474px; background: var(--red); color: var(--white); font-family: "Lato", sans-serif; }
  .card__panel { position: absolute; inset: 0; width: 100%; height: 100%; }
  .division-mark { position: absolute; left: 430px; top: 120px; display: flex; align-items: center; gap: 12px; }
  .division-mark__dot { width: 20px; height: 20px; border-radius: 50%; background: var(--red-soft); flex: none; }
  .division-mark__name {
    font-family: "Montserrat", sans-serif; font-weight: 900; font-size: 30px;
    color: var(--red); line-height: 1.05;
  }

  .contact { position: absolute; left: 34px; top: 46px; }
  .contact__name {
    font-family: "Montserrat", sans-serif; font-weight: 900; font-size: 32px;
    letter-spacing: .5px; margin-bottom: 10px; white-space: nowrap;
  }
  .contact__list { list-style: none; }
  .contact__list li { display: flex; align-items: center; gap: 10px; font-size: 17px; line-height: 28px; white-space: nowrap; }
  .contact__list svg { width: 15px; height: 15px; flex: none; }

  .services { position: absolute; left: 34px; top: 208px; }
  .services__title { font-family: "Montserrat", sans-serif; font-weight: 900; font-size: 24px; margin-bottom: 6px; white-space: nowrap; }
  .services .tick-list li { font-size: 17px; line-height: 28px; }

  .tagline { position: absolute; left: 34px; top: 338px; font-weight: 900; font-size: 16px; line-height: 21px; white-space: nowrap; }
</style>
</head>
<body>
<main class="canvas">

  <!-- Side 1 -->
  <section class="card card--training" aria-label="Summit Relay training side">
    <div class="brand-lockup">
      <span class="brand-lockup__mark"></span>
      <span class="brand-lockup__name">SUMMIT<br>RELAY</span>
    </div>
    <div class="brand-rule"></div>

    <div class="training">
      <h2 class="training__title">OUR TRAINING</h2>
      <ul class="tick-list">
        <li><svg viewBox="0 0 14 14"><circle cx="7" cy="7" r="7" fill="#f01418"/><path d="M3.8 7.2l2.2 2.1 4.2-4.4" stroke="#1c1c1c" stroke-width="1.8" fill="none"/></svg>Fire Training</li>
        <li><svg viewBox="0 0 14 14"><circle cx="7" cy="7" r="7" fill="#f01418"/><path d="M3.8 7.2l2.2 2.1 4.2-4.4" stroke="#1c1c1c" stroke-width="1.8" fill="none"/></svg>Confined Space Rescue Training</li>
        <li><svg viewBox="0 0 14 14"><circle cx="7" cy="7" r="7" fill="#f01418"/><path d="M3.8 7.2l2.2 2.1 4.2-4.4" stroke="#1c1c1c" stroke-width="1.8" fill="none"/></svg>Rope Rescue Training</li>
        <li><svg viewBox="0 0 14 14"><circle cx="7" cy="7" r="7" fill="#f01418"/><path d="M3.8 7.2l2.2 2.1 4.2-4.4" stroke="#1c1c1c" stroke-width="1.8" fill="none"/></svg>Hazmat Training | EMS</li>
        <li><svg viewBox="0 0 14 14"><circle cx="7" cy="7" r="7" fill="#f01418"/><path d="M3.8 7.2l2.2 2.1 4.2-4.4" stroke="#1c1c1c" stroke-width="1.8" fill="none"/></svg>Incident Command</li>
        <li><svg viewBox="0 0 14 14"><circle cx="7" cy="7" r="7" fill="#f01418"/><path d="M3.8 7.2l2.2 2.1 4.2-4.4" stroke="#1c1c1c" stroke-width="1.8" fill="none"/></svg>Pump Operations Training</li>
      </ul>
    </div>

    <p class="website">WWW.SUMMITRELAY-EXAMPLE.COM</p>
  </section>

  <!-- Side 2 -->
  <section class="card card--field" aria-label="Summit Relay field services side">
    <svg class="card__panel" viewBox="0 0 700 400" preserveAspectRatio="none" aria-hidden="true">
      <polygon points="395,0 700,0 700,210 430,400 395,400 370,220" fill="var(--paper)"/>
    </svg>

    <div class="division-mark">
      <span class="division-mark__dot"></span>
      <span class="division-mark__name">SUMMIT<br>RELAY</span>
    </div>

    <div class="contact">
      <h1 class="contact__name">DANIEL BROOKS</h1>
      <ul class="contact__list">
        <li><svg viewBox="0 0 16 16"><path d="M4 1.5l2.5 3-1.5 1.8a9 9 0 0 0 4.7 4.7L11.5 9.5l3 2.5-1.5 2.5C7.5 14.5 1.5 8.5 1.5 3z" fill="#fff"/></svg>(555) 014-2290</li>
        <li><svg viewBox="0 0 16 16"><rect x="1" y="3" width="14" height="10" fill="#fff"/><path d="M1 3l7 6 7-6" stroke="#f01418" stroke-width="1.4" fill="none"/></svg>info@summitrelay-example.com</li>
        <li><svg viewBox="0 0 16 16"><circle cx="8" cy="8" r="7" fill="#fff"/><path d="M1 8h14M8 1c-3 3.5-3 10.5 0 14M8 1c3 3.5 3 10.5 0 14" stroke="#f01418" stroke-width="1.1" fill="none"/></svg>summitrelay-example.com</li>
      </ul>
    </div>

    <div class="services">
      <h2 class="services__title">FIELD SERVICES</h2>
      <ul class="tick-list">
        <li><svg viewBox="0 0 14 14"><circle cx="7" cy="7" r="7" fill="#fff"/><path d="M3.8 7.2l2.2 2.1 4.2-4.4" stroke="#f01418" stroke-width="1.8" fill="none"/></svg>Fire Department</li>
        <li><svg viewBox="0 0 14 14"><circle cx="7" cy="7" r="7" fill="#fff"/><path d="M3.8 7.2l2.2 2.1 4.2-4.4" stroke="#f01418" stroke-width="1.8" fill="none"/></svg>Stand-by Rescue</li>
        <li><svg viewBox="0 0 14 14"><circle cx="7" cy="7" r="7" fill="#fff"/><path d="M3.8 7.2l2.2 2.1 4.2-4.4" stroke="#f01418" stroke-width="1.8" fill="none"/></svg>Safety | EMS | Planning</li>
      </ul>
    </div>

    <p class="tagline">Supporting the Emergency<br>Response Community Since 1967</p>
  </section>

</main>
</body>
</html>
```